Marketing Campaign Brochure Design KPT BI

Create a Brochure for a marketing campaign on a new product.

Korrin Pathway Trust is a Electrical engineering consulting and contracting company specialising in integrating and unifying technical solutions. Please go to www.korrinpathwaytrust.com.au for a "philosophy" of this company to give you a feel for the company.

Please keep in mind that I have also posted a project to refresh this website with the new logo which I will upload to this project.

This campaign is based on a "Business Intelligence" product which provides reports based on data gathered from a client (e.g. in hospitals, emergency call system alarms, security alarms, fire alarms, people counter etc...) and produces management reports based on standard KPI's in the industry and management initiatives.

Please produce a brochure for this marketing campaign based around the logo attached and your creativity. The feel will be fresh, modern, simple yes technology & business analytical and intuitave...

Thank you for taking the time to assist on this project.

Regards,
Mai Tovar.

Industry/Entity Type

Marketing

Requirements
Must have
• Must have the Logo of the company incorporated. Logo will be uploaded.

However the "Business Intelligence" marketing campaign will have a secondary logo for marketing purposes. It is a Seperate department of the Korrin Pathway Trust.

e.g. Korrin Pathway Trust, Business Intelligence Department.

```html
<!DOCTYPE html>
<html lang="en">
<head>
<meta charset="utf-8">
<title>KPT BI Brochure</title>
<link href="https://fonts.googleapis.com/css2?family=Arimo:wght@400;700&display=swap" rel="stylesheet">
<style>
  :root{
    --page-bg:#e6e6e6;
    --paper:#ffffff;
    --ink:#141a22;
    --navy:#1d2a6b;
    --panel:rgba(52,176,236,0.88);
    --panel-text:#ffffff;
    --accent-lime:#d8e24a;
    --band-blue:#5b8fc9;
    --mist-1:#f4f7fa;
    --mist-2:#c9d6e3;
    --mist-3:#8ea4bc;
  }
  *{margin:0;padding:0;box-sizing:border-box}
  html,body{width:1200px;height:900px;overflow:hidden}
  body{background:var(--page-bg);font-family:"Arimo",Arial,sans-serif;color:var(--ink)}
  .brochure{position:absolute;left:293px;top:20px;width:613px;height:860px;background:var(--paper);overflow:hidden}
  .hero-photo{position:absolute;left:0;top:0;width:613px;height:215px;
    background:linear-gradient(160deg,#d9dde2 0%,#f3f4f6 35%,#b8bec6 60%,#6d737c 100%)}
  .swoosh{position:absolute;left:0;top:140px;width:613px;height:110px}
  .data-backdrop{position:absolute;left:0;top:215px;width:613px;height:530px;
    background:radial-gradient(ellipse at 75% 30%,var(--mist-1) 0%,var(--mist-2) 45%,var(--mist-3) 100%);
    -webkit-mask-image:linear-gradient(to bottom,#000 70%,transparent 100%);
    mask-image:linear-gradient(to bottom,#000 70%,transparent 100%)}
  .section-title{position:absolute;font-weight:700;color:var(--ink);line-height:1.1}
  .value-title{left:52px;top:275px;font-size:25px}
  .facilities-title{left:210px;top:480px;width:360px;font-size:23px}
  .panel{position:absolute;background:var(--panel);color:var(--panel-text);font-size:12.5px;line-height:1.35}
  .value-panel{left:42px;top:308px;width:325px;height:128px;padding:14px 14px}
  .facilities-panel{left:200px;top:532px;width:367px;height:176px;padding:10px 14px 10px 14px}
  .facilities-panel ul{list-style:none}
  .facilities-panel li{position:relative;padding-left:13px;margin-bottom:9px}
  .facilities-panel li::before{content:"";position:absolute;left:0;top:6px;width:4px;height:4px;border-radius:50%;background:var(--panel-text)}
  .contact{position:absolute;left:30px;top:748px;font-size:11px;line-height:1.35}
  .contact-label{font-weight:700;margin-bottom:8px}
  .contact b{font-weight:700}
  .brand{position:absolute;left:330px;top:740px;display:flex;align-items:center;gap:10px}
  .brand-mark{width:46px;height:46px;border-radius:50%;background:var(--navy)}
  .brand-name{font-size:22px;font-weight:700;color:var(--navy);line-height:1}
  .website{position:absolute;left:342px;top:833px;font-size:13px;color:var(--ink)}
</style>
</head>
<body>
  <article class="brochure">
    <div class="hero-photo" role="img" aria-label="Photo of business people reviewing printed reports and charts beside a computer screen"></div>
    <svg class="swoosh" viewBox="0 0 613 110" aria-hidden="true">
      <path d="M0 60 C200 95 420 40 613 0 L613 110 L0 110 Z" fill="#ffffff"/>
      <path d="M0 58 C210 92 420 38 613 -2 L613 10 C420 55 210 105 0 72 Z" fill="var(--band-blue)" opacity="0.55"/>
      <path d="M0 56 C210 88 420 34 613 -6" fill="none" stroke="var(--accent-lime)" stroke-width="4"/>
    </svg>
    <div class="data-backdrop" role="img" aria-label="Close-up of a keyboard overlaid with faint binary digits in soft blue tones"></div>

    <h2 class="section-title value-title">Value Proposition</h2>
    <div class="panel value-panel">
      <p>Business Intelligence Department within the Korrin Pathway Trust (BI Team) that adds value to healthcare for Hospitals and Aged Care Facilities. This business unit will provide the hardware and software systems that produce the higher level integration and reporting that is required.</p>
    </div>

    <h2 class="section-title facilities-title">Development of the following reporting facilities</h2>
    <div class="panel facilities-panel">
      <ul>
        <li>Development of a reporting server which can generate reports that is easy to use for the client.</li>
        <li>Web based GUI.</li>
        <li>This system can print out reports as a pdf or a spreadsheet for further analysis.</li>
        <li>Reporting will have graphs and trend charts.</li>
        <li>Reporting will have industry standards for metric</li>
      </ul>
    </div>

    <address class="contact" style="font-style:normal">
      <p class="contact-label">CONTACT:</p>
      <p>KPT PTY. LTD.</p>
      <p>P.O.Box 418 Glebe, NSW,</p>
      <p>Australia 2037</p>
      <p><b>ACN</b> 162 905 318</p>
      <p><b>ABN</b> 34 162 905 318</p>
      <p><b>FAX</b> +61 2 9000 4187</p>
    </address>

    <div class="brand">
      <span class="brand-mark" aria-hidden="true"></span>
      <span class="brand-name">Korrin Pathway Trust</span>
    </div>
    <p class="website">www.korrinpathwaytrust.com.au</p>
  </article>
</body>
</html>
```